Design for company homepage promoting to the pharmaceutical industry

Our company produces medical education materials and services for the pharmaceutical industry. Our existing website (www.quorvane.net.au) provides more information.
 
We need a homepage design for our new company website we are creating. Our site will not have a great amount of content, we want it to be fast, user friendly and easily adaptable to viewing on any platform, and through any browser. We don't want it over-designed - i.e. no highly animated banner flags, backgrounds, obscure webfonts, too many graphics etc. Attached are files indicating our existing company logo and design. We want the logo and rings to be retained. We've also attached draft copy for the website.
The final website may be designed in Wordpress (still to be confirmed)
 
This is a design to replace the current site (www.quorvane.net.au). Content will also be revised.
Things we don't like about our current design - doesn't use our current branding, is not very exciting, old fashioned 'standard' format, too much content, just doesn't look that good, boring.
 
Examples of sites we like:
www.bralimo.com.au
http://factsheets.tenvoramed.com.au/index.html
 
Features we like from these sites - fast, responsive, short and to the point, cross-platform compatible including smartphones, and looks good
 
Main reasons people will visit our site: to find out whether we can provide services they might be looking for, to make a decision on whether they are interested in what we offer so they can get in touch with us, and to get our contact details.
Main thing we want to achieve from website visits is that it looks good enough and provides enough summary information on us so that they want to get in touch with us, to offer us work or to ask us to come in and meet them to provide more info on what we do.
Two most important calls to action from our website
· make the decision that we can do what you are looking for
· get in touch with us.
Updates

Thanks everyone for your submissions. At this stage with the Christmas break upon us, we are yet to finalise our decision, and will make a decision early in the new year. I hope everyone has a good holiday break.
Kind regards
Giles

Target Market(s)

Pharmaceutical industry professionals, marketers and medical professionals.

Industry/Entity Type

Pharmaceutical

Requirements
Must have
• Company logo and rings must be incorporated, company colour - blue - must be in there.
Should not have
• Complex animation or graphics that will slow the upload or limit cross-platform compatability/viewing on smartphones etc.

```html
<!DOCTYPE html>
<html lang="en">
<head>
<meta charset="utf-8">
<title>Quorvane Healthcare Education</title>
<link rel="stylesheet" href="https://fonts.googleapis.com/css2?family=Lato:wght@300;400;700&display=swap">
<style>
:root{
  --brand:#0b4a85;
  --text:#444;
  --muted:#777;
  --client:#666;
  --panel:#f0f0f0;
  --card-border:#dedede;
  --icon:#8a8a8a;
  --footer-bar:#3d3d40;
  --white:#fff;
  --black:#000;
}
*{box-sizing:border-box;margin:0;padding:0}
html,body{width:924px;height:1200px;overflow:hidden;background:var(--white);font-family:'Lato',sans-serif;color:var(--text)}
.page{position:relative;width:924px;height:1200px}
.abs{position:absolute}

/* header */
.brand{left:100px;top:44px;font-size:26px;line-height:28px;font-weight:400;color:var(--brand)}
.search{left:699px;top:15px;width:138px;height:20px;background:#555;display:flex}
.search span{flex:1;color:#eee;font-size:11px;line-height:20px;padding-left:7px}
.search b{width:18px;background:var(--brand);display:flex;align-items:center;justify-content:center}
.nav-link{top:59px;font-size:11px;letter-spacing:.8px;color:var(--muted);text-decoration:none;height:38px;white-space:nowrap}
.nav-link.current{color:var(--brand)}
.nav-link.current::after{content:"";position:absolute;left:-3px;right:-3px;bottom:0;height:4px;background:var(--brand)}

/* hero */
.hero{left:9px;top:97px;width:906px;height:384px;background:radial-gradient(ellipse at 50% 70%,#19d7e8 0%,#2cb9d6 30%,#4aa6cf 55%,#7a7fb6 85%,#8a6fa8 100%)}
.hero-copy{left:9px;width:906px;text-align:center;color:var(--white);font-weight:300;white-space:nowrap}
.hero-h1{top:193px;font-size:35px;line-height:42px}
.hero-h2{top:249px;font-size:19px;line-height:24px}
.hero-h3{top:305px;font-size:15px;line-height:20px}
.hero-h4{top:327px;font-size:25px;line-height:32px}
.hero-btn{left:384px;top:387px;width:166px;height:36px;background:var(--white);color:var(--brand);font-size:21px;text-align:center;line-height:36px}
.arrow{top:288px}
.hero-rule{left:9px;top:480px;width:906px;height:6px;background:var(--brand)}

/* services */
.services{left:9px;top:486px;width:906px;height:287px;background:var(--panel)}
.card{top:524px;width:240px;height:222px;background:var(--white);border:1px solid var(--card-border);text-align:center}
.card-icon{margin:40px auto 0;width:40px;height:44px;display:block}
.card h2{font-weight:400;font-size:16px;line-height:20px;color:var(--brand);margin-top:14px;letter-spacing:.2px}
.card p{font-size:11px;line-height:14px;margin:20px 20px 0;color:#333}

/* clients */
.clients-rule{top:815px;height:1px;background:var(--brand)}
.clients-title{left:0;width:924px;top:803px;text-align:center;font-size:19px;line-height:24px;font-weight:300;color:var(--brand);letter-spacing:1px}
.client{top:879px;height:26px;font-size:18px;line-height:26px;font-weight:700;color:var(--client);text-align:center;white-space:nowrap}

/* footer */
.footer-shape{left:9px;top:972px}
.footer-glow{left:200px;top:985px;width:460px;height:165px;border-radius:50%;background:radial-gradient(ellipse,rgba(255,255,255,.08),rgba(255,255,255,0) 70%)}
.footer-col{top:1004px;color:var(--white)}
.footer-col h3{font-size:10px;line-height:12px;font-weight:700;margin-bottom:12px}
.tweet{display:flex;gap:12px;margin-bottom:8px;font-size:8px;font-weight:700;line-height:11px}
.tweet i{width:14px;height:14px;border-radius:50%;background:var(--white);flex:none;margin-top:4px}
.tweet small{display:block;font-size:5px;font-weight:400;opacity:.8}
.tweet em{font-style:normal;opacity:.75}
.newsletter p{font-size:7px;line-height:12px;width:170px}
.news-field{margin-top:6px;display:flex;align-items:center;gap:4px}
.news-field span{width:126px;border-bottom:1px solid var(--white);height:12px}
.news-field b{width:14px;height:13px;border:1px solid var(--white);display:block;background:var(--black)}
.social{display:flex;gap:3px}
.social i{width:22px;height:22px;background:var(--black);display:block}
.contact-row{display:flex;gap:10px;font-size:7px;line-height:11px;margin-bottom:12px}
.contact-row i{width:16px;height:16px;background:var(--black);flex:none;display:flex;align-items:center;justify-content:center}
.contact-row u{text-decoration:underline}
.footer-bar{left:9px;top:1152px;width:906px;height:38px;background:var(--footer-bar);color:var(--white);font-size:8px;font-weight:700;line-height:38px}
</style>
</head>
<body>
<div class="page">

  <header>
    <div class="abs brand">quorvane</div>
    <div class="abs search"><span>Search Me</span>
      <b><svg width="9" height="9" viewBox="0 0 10 10"><circle cx="4" cy="4" r="3" fill="none" stroke="#fff" stroke-width="1.5"/><path d="M6.3 6.3 9 9" stroke="#fff" stroke-width="1.6"/></svg></b>
    </div>
    <nav>
      <a class="abs nav-link current" style="left:318px">Home</a>
      <a class="abs nav-link" style="left:381px">Who We Are</a>
      <a class="abs nav-link" style="left:481px">What We Do</a>
      <a class="abs nav-link" style="left:581px">Our Work</a>
      <a class="abs nav-link" style="left:667px">Our Client</a>
      <a class="abs nav-link" style="left:757px">Contact Us</a>
    </nav>
  </header>

  <section>
    <div class="abs hero" role="img" aria-label="Photograph of rippling turquoise water"></div>
    <p class="abs hero-copy hero-h1">We are healthcare communication specialists;</p>
    <p class="abs hero-copy hero-h2">this means we’re scientists, journalists and marketers rolled into one.</p>
    <p class="abs hero-copy hero-h3">Discover elegant solution for your business</p>
    <p class="abs hero-copy hero-h4">fast, reliable, affordable!</p>
    <a class="abs hero-btn">contact us</a>
    <svg class="abs arrow" style="left:17px" width="24" height="22" viewBox="0 0 24 22"><path d="M12 1 2 11l10 10M2 11h22" fill="none" stroke="#fff" stroke-width="1.6"/></svg>
    <svg class="abs arrow" style="left:877px" width="24" height="22" viewBox="0 0 24 22"><path d="M12 1l10 10-10 10M22 11H0" fill="none" stroke="#fff" stroke-width="1.6"/></svg>
    <div class="abs hero-rule"></div>
  </section>

  <section>
    <div class="abs services"></div>
    <svg class="abs" style="left:446px;top:486px" width="32" height="20" viewBox="0 0 32 20"><path d="M0 0h32c-8 0-12 4-16 18C12 4 8 0 0 0z" fill="#0b4a85"/></svg>
    <svg class="abs" style="left:440px;top:773px" width="44" height="18" viewBox="0 0 44 18"><path d="M0 0h44c-10 0-16 4-22 16C16 4 10 0 0 0z" fill="#f0f0f0"/></svg>

    <article class="abs card" style="left:85px">
      <div class="card-icon" role="img" aria-label="Icon of a team member" style="background:var(--icon);border-radius:8px 8px 2px 2px"></div>
      <h2>WHO WE ARE</h2>
      <p>Lorem ipsum dolor a sit eget amet, consectetur adipiscing elit in sit amet aliquet odio, nec vehicula leo.</p>
    </article>
    <article class="abs card" style="left:342px">
      <svg class="card-icon" viewBox="0 0 40 44"><rect x="3" y="4" width="34" height="39" fill="#8a8a8a"/><rect x="7" y="9" width="26" height="30" fill="#fff"/><rect x="14" y="1" width="12" height="6" fill="#8a8a8a"/><path d="M11 16h18M11 21h18M11 26h18M11 31h12" stroke="#8a8a8a" stroke-width="2"/></svg>
      <h2>WHAT WE DO</h2>
      <p>Lorem ipsum dolor a sit eget amet, consectetur adipiscing elit in sit amet aliquet odio, nec vehicula leo.</p>
    </article>
    <article class="abs card" style="left:598px">
      <svg class="card-icon" viewBox="0 0 40 44"><g fill="#8a8a8a"><rect x="4" y="4" width="30" height="8" rx="2"/><rect x="6" y="14" width="30" height="8" rx="2"/><rect x="4" y="24" width="30" height="8" rx="2"/><rect x="6" y="34" width="30" height="8" rx="2"/></g></svg>
      <h2>OUR WORK</h2>
      <p>Lorem ipsum dolor a sit eget amet, consectetur adipiscing elit in sit amet aliquet odio, nec vehicula leo.</p>
    </article>
  </section>

  <section>
    <div class="abs clients-rule" style="left:85px;width:322px"></div>
    <div class="abs clients-rule" style="left:517px;width:320px"></div>
    <h2 class="abs clients-title">CLIENTS</h2>
    <div class="abs client" style="left:122px;width:100px">Wendmore</div>
    <div class="abs client" style="left:232px;width:100px">Lumeva</div>
    <div class="abs client" style="left:348px;width:150px">Castor-Brandt</div>
    <div class="abs client" style="left:528px;width:130px">Norvatic</div>
    <div class="abs client" style="left:684px;width:100px">Paylume</div>
  </section>

  <footer>
    <svg class="abs footer-shape" width="906" height="181" viewBox="0 0 906 181">
      <path d="M0 0H181a12 12 0 0 1 12 12a12 12 0 0 1 12-12H436a12 12 0 0 1 12 12a12 12 0 0 1 12-12H693a12 12 0 0 1 12 12a12 12 0 0 1 12-12H906V181H0Z" fill="#0b4a85"/>
    </svg>
    <div class="abs footer-glow" role="img" aria-label="Faint water ripple backdrop"></div>

    <div class="abs footer-col" style="left:85px;width:220px">
      <h3>Latest tweets</h3>
      <div class="tweet"><i></i><div>Check Out Tobrin's <em>@Kelvanto</em> Sales Notification<br>http://lnk.qv/ R8TmQe2P<small>3 days ago</small></div></div>
      <div class="tweet"><i></i><div>Community Superstar Winner – <em>#MeadowHiveMedia</em><br>http://lnk.qv/7Hd2kLw<small>3 days ago</small></div></div>
      <div class="tweet"><i></i><div>Clean <em>#Websites</em> Designs for Your <em>#Inspiration</em><br>http://lnk.qv/ 9xVb4Tn<small>3 days ago</small></div></div>
    </div>

    <div class="abs footer-col newsletter" style="left:341px;width:200px">
      <h3>Newsletter</h3>
      <p>Lorem Ipsum is simply dummy text of the printing and typesetting industry.</p>
      <div class="news-field"><span></span><b></b></div>
      <h3 style="margin-top:24px">Social Connecting</h3>
      <div class="social"><i></i><i></i><i></i></div>
    </div>

    <div class="abs footer-col" style="left:598px;width:240px">
      <h3>Contact info</h3>
      <div class="contact-row"><i><svg width="7" height="9" viewBox="0 0 7 9"><path d="M3.5 9C1 5.5 0 4.5 0 3.5a3.5 3.5 0 0 1 7 0C7 4.5 6 5.5 3.5 9z" fill="#fff"/></svg></i><div>Address: 4821 Rue des Ormeaux,<br>69040 Lyonnet, France</div></div>
      <div class="contact-row"><i><svg width="9" height="9" viewBox="0 0 9 9"><circle cx="4.5" cy="4.5" r="4" fill="none" stroke="#fff"/></svg></i><div>Phone: +00 000 555-01-23<br>&nbsp;&nbsp;&nbsp;&nbsp;&nbsp;&nbsp;&nbsp;&nbsp;&nbsp;&nbsp;&nbsp;+00 000 555-01-24</div></div>
      <div class="contact-row"><i><svg width="9" height="7" viewBox="0 0 9 7"><rect width="9" height="7" fill="#fff"/><path d="M0 0l4.5 4L9 0" stroke="#000" fill="none"/></svg></i><div style="padding-top:3px">E-mail: <u>support@quorvane.net.au</u></div></div>
    </div>

    <div class="abs footer-bar">
      <span style="position:absolute;left:78px">Copyright 2013 - www.quorvane.com - All Rights Reserved</span>
      <span style="position:absolute;right:85px">Privacy &nbsp;|&nbsp; Terms &amp; Condition</span>
    </div>
  </footer>

</div>
</body>
</html>
```